Infographic to explain our offering

We are a cloudvantix.com partner and would like to issue an infographic to our business partners who recommend our services. A one page, A4 graphic, simple and in our colours of blue background and white (clean) images. to cover such things as;

+ UK map (white areas of where we operate)
+ Simple outline icons of the sectors / industries we operate in
+ A simple graphic of number of projects we have completed (500+)
+ A simple graphic of number of years we have been operating (9+)
+ Product areas we work with being, Deal Harbor, Help Harbor, Zembly
+ Services we offer, Consulting to Enterprise and SMB, Training and Support (also, data migration and data integration)
+ Certifications we hold (we have images from Cloudvantix.com that we can incorporate)
+ Broad areas we consult in being, CRM, Marketing Automation and Social Media Engagement
+Maybe something around our specific offerings for SMB market being, QuickLaunch (Bronze, Silver, Gold), showing average days for each. Single Sprint Boost

Open to other suggestions

Sectors we operate in;

SMB (up-to £100m)
Professional Services
Marketing / Media
Engineering / Manufacturing
Construction
Healthcare
Financial Services / Investments
Membership

Major UK areas

London (40%)
South East (25%)
Manchester (and surrounding areas) (25%)
Birmingham (and surrounding areas) (10%)

Offices
London
Birmingham
Manchester

More styling ideas and information about our offering and company can be found here

www.tarnwellpartners.example

Industry/Entity Type

Business

Font styles to use
Sans Serif

Colors
33a6d7
0692cd
0655a3
ffffff

Requirements
Must have
• Clean and clear messages
Should not have
• Too much text

```html
<!DOCTYPE html>
<html lang="en">
<head>
<meta charset="utf-8">
<title>Sectors we operate in</title>
<link rel="stylesheet" href="https://fonts.googleapis.com/css2?family=Arimo:wght@400&display=swap">
<style>
  :root {
    --sky: #2e9cdc;
    --white: #ffffff;
  }
  html, body {
    margin: 0;
    padding: 0;
    width: 1200px;
    height: 849px;
    overflow: hidden;
    background: var(--sky);
  }
  .sheet {
    position: relative;
    width: 1200px;
    height: 849px;
    background: var(--sky);
    color: var(--white);
    font-family: "Arimo", Arial, sans-serif;
    overflow: hidden;
  }
  .sheet__title {
    position: absolute;
    left: 80px;
    top: 58px;
    margin: 0;
    font-weight: 400;
    font-size: 54px;
    line-height: 1;
    letter-spacing: -0.2px;
    white-space: nowrap;
  }
  .sheet__ampersand {
    position: absolute;
    left: 208px;
    top: 216px;
    font-size: 191px;
    line-height: 1;
  }
  .sectors {
    position: absolute;
    left: 80px;
    top: 513px;
  }
  .sectors__heading {
    margin: 0 0 11px;
    font-weight: 400;
    font-size: 36px;
    line-height: 1;
    white-space: nowrap;
  }
  .sectors__list {
    list-style: none;
    margin: 0;
    padding: 0;
    font-size: 18.4px;
    line-height: 22.4px;
    white-space: nowrap;
  }
  .offering {
    position: absolute;
    left: 0;
    top: 0;
    width: 1200px;
    height: 849px;
  }
  .offering__ring {
    fill: none;
    stroke: var(--white);
  }
  .offering__label {
    fill: var(--white);
    font-family: "Arimo", Arial, sans-serif;
    font-size: 18.3px;
    text-anchor: end;
  }
  .offering__icon-disc { fill: var(--white); }
  .offering__icon-glyph { fill: none; stroke: var(--sky); stroke-width: 2.2; stroke-linecap: round; stroke-linejoin: round; }
  .offering__icon-fill { fill: var(--sky); }
</style>
</head>
<body>
<main class="sheet">
  <h1 class="sheet__title">Sectors we operate in:</h1>
  <div class="sheet__ampersand" aria-hidden="true">&amp;</div>

  <section class="sectors">
    <h2 class="sectors__heading">Professional services:</h2>
    <ul class="sectors__list">
      <li>- SMB (up-to £100m)</li>
      <li>- Professional Services</li>
      <li>- Marketing / Media</li>
      <li>- Engineering / Manufacturing</li>
      <li>- Construction</li>
      <li>- Healthcare</li>
      <li>- Financial Services / Investments</li>
      <li>- Membership</li>
    </ul>
  </section>

  <svg class="offering" viewBox="0 0 1169 827" preserveAspectRatio="none" aria-label="Offering rings">
    <defs>
      <radialGradient id="map-tone" cx="50%" cy="45%" r="65%">
        <stop offset="0%" stop-color="#ffffff" stop-opacity="0.95"/>
        <stop offset="100%" stop-color="#ffffff" stop-opacity="0.7"/>
      </radialGradient>
    </defs>

    <g class="offering__rings">
      <path class="offering__ring" stroke-width="17" d="M789 153 A295 295 0 1 1 580.4 239.4"/>
      <path class="offering__ring" stroke-width="16" d="M789 181 A267 267 0 1 1 551.1 326.8"/>
      <path class="offering__ring" stroke-width="15" d="M789 208 A240 240 0 1 1 563.5 365.9"/>
      <path class="offering__ring" stroke-width="14" d="M789 233 A215 215 0 1 1 574.1 455.5"/>
      <path class="offering__ring" stroke-width="13" d="M789 255 A193 193 0 1 1 636.9 566.8"/>
      <path class="offering__ring" stroke-width="12" d="M789 278 A170 170 0 1 1 684.3 582.0"/>
      <path class="offering__ring" stroke-width="11" d="M789 300 A148 148 0 1 1 750.7 591.0"/>
      <path class="offering__ring" stroke-width="10" d="M789 321 A127 127 0 1 1 699.2 358.2"/>
    </g>

    <g class="offering__labels">
      <text class="offering__label" x="773" y="159">9+ Years</text>
      <text class="offering__label" x="773" y="187">500+ Projects</text>
      <text class="offering__label" x="773" y="214">Enterprise consulting</text>
      <text class="offering__label" x="773" y="239">SMB</text>
      <text class="offering__label" x="773" y="261">Training &amp; Support</text>
      <text class="offering__label" x="773" y="284">CRM</text>
      <text class="offering__label" x="773" y="306">Marketing Automation</text>
      <text class="offering__label" x="773" y="327">Social Media Engagement</text>
    </g>

    <ellipse class="offering__map" role="img"
             aria-label="White map of the United Kingdom and Ireland showing where we operate"
             cx="790" cy="435" rx="68" ry="88" fill="url(#map-tone)"/>

    <g class="offering__icon" aria-label="Cloud sync">
      <circle class="offering__icon-disc" cx="727" cy="382" r="18"/>
      <path class="offering__icon-glyph" d="M718 389 h17 a5 5 0 0 0 0-10 a7 7 0 0 0-13-2 a5 5 0 0 0-4 12 z"/>
      <circle class="offering__icon-fill" cx="727" cy="384" r="2.5"/>
    </g>

    <g class="offering__icon" aria-label="People">
      <circle class="offering__icon-disc" cx="878" cy="428" r="18"/>
      <circle class="offering__icon-fill" cx="878" cy="422" r="4"/>
      <path class="offering__icon-fill" d="M870 436 a8 7 0 0 1 16 0 z"/>
      <circle class="offering__icon-fill" cx="869" cy="424" r="3"/>
      <circle class="offering__icon-fill" cx="887" cy="424" r="3"/>
    </g>

    <g class="offering__icon" aria-label="Partnership">
      <circle class="offering__icon-disc" cx="741" cy="525" r="18"/>
      <path class="offering__icon-glyph" d="M728 523 l6-5 l7 4 l7-4 l6 5 M734 527 l6 5 l8-6"/>
    </g>
  </svg>
</main>
</body>
</html>
```